Modern stationary/business card design for KRM Interior Solutions
KRM Interior Solutions
Modern
Lowell Brascombe
VP
2847 B Ferncliff
Marlowe Springs, TX 75590
lowell@stoneworkhaven.com
www.stoneworkhaven.com
We are open to tag lines so feel free to explore. I will give feedback to point you in the right direction.
Possibly a list of all the services we provide...
Granite, Quartz, Tile, Vinyl, Wood, Carpet, Mirrors, Cabinets, Hardware
I have more colors to choose from.

```html
<!DOCTYPE html>
<html lang="en">
<head>
<meta charset="utf-8">
<title>KRM Interior Solutions – Business Card</title>
<link rel="stylesheet" href="https://fonts.googleapis.com/css2?family=Open+Sans:wght@400;600&family=Arimo:wght@400;700&display=swap">
<style>
  :root {
    --backdrop: #4a4949;
    --card: #ffffff;
    --brand-blue: #4a80b0;
    --tab-blue: #4f82ad;
    --ink: #1d1d1d;
    --muted: #8a8a8a;
    --tag-grey: #6f6f6f;
    --divider: #b9b9b9;
  }
  * { box-sizing: border-box; margin: 0; padding: 0; }
  html, body {
    width: 1200px; height: 780px; overflow: hidden;
    background: var(--backdrop);
  }
  .card {
    position: absolute; left: 170px; top: 165px;
    width: 860px; height: 450px;
    background: var(--card);
    border-radius: 26px;
    box-shadow: 0 6px 18px rgba(0,0,0,.35);
    font-family: "Arimo", Arial, sans-serif;
  }
  .edge-tab {
    position: absolute; width: 15px; height: 140px;
    background: var(--tab-blue);
  }
  .edge-tab--left { left: 0; top: 230px; border-radius: 0 10px 10px 0; }
  .edge-tab--right { right: 0; top: 105px; border-radius: 10px 0 0 10px; }

  .brand {
    position: absolute; left: 0; top: 0; width: 390px; height: 100%;
    display: flex; flex-direction: column; align-items: center; justify-content: center;
    font-family: "Open Sans", Arial, sans-serif; font-weight: 400;
  }
  .brand__mark {
    width: 84px; height: 84px; background: var(--brand-blue);
    margin-bottom: 22px;
  }
  .brand__name { font-size: 70px; line-height: 1; letter-spacing: 1px; color: var(--brand-blue); }
  .brand__tag { font-size: 22px; line-height: 1.3; margin-top: 4px; color: var(--tag-grey); }

  .divider {
    position: absolute; left: 392px; top: 30px; width: 3px; height: 390px;
    background: linear-gradient(to bottom, rgba(185,185,185,0), var(--divider) 30%, var(--divider) 70%, rgba(185,185,185,0));
  }

  .contact {
    position: absolute; left: 432px; top: 92px; right: 40px;
    color: var(--ink);
  }
  .contact__name {
    font-size: 25px; font-weight: 400; color: var(--brand-blue); letter-spacing: .5px;
    -webkit-text-stroke: .4px var(--brand-blue);
  }
  .contact__role { font-size: 16px; color: var(--muted); margin-top: 14px; }
  .contact__address { font-size: 18px; line-height: 1.3; margin-top: 28px; }
  .contact__lines { list-style: none; margin-top: 34px; }
  .contact__line {
    display: flex; align-items: center; gap: 12px;
    font-size: 18px; line-height: 1.5;
  }
  .contact__icon { width: 18px; height: 18px; fill: var(--brand-blue); flex: none; }
</style>
</head>
<body>
  <div class="card">
    <div class="edge-tab edge-tab--left"></div>
    <div class="edge-tab edge-tab--right"></div>

    <div class="brand">
      <div class="brand__mark"></div>
      <div class="brand__name">KRM</div>
      <div class="brand__tag">Interior Solutions</div>
    </div>

    <div class="divider"></div>

    <div class="contact">
      <div class="contact__name">Lowell Brascombe</div>
      <div class="contact__role">VP</div>
      <div class="contact__address">2847 B Ferncliff Marlowe Springs,<br>TX 75590</div>
      <ul class="contact__lines">
        <li class="contact__line">
          <svg class="contact__icon" viewBox="0 0 24 24"><path d="M6.6 10.8a15 15 0 0 0 6.6 6.6l2.2-2.2a1 1 0 0 1 1-.25 11.4 11.4 0 0 0 3.6.57 1 1 0 0 1 1 1V20a1 1 0 0 1-1 1A17 17 0 0 1 3 4a1 1 0 0 1 1-1h3.5a1 1 0 0 1 1 1c0 1.25.2 2.45.57 3.57a1 1 0 0 1-.25 1z"/></svg>
          555-014-2736
        </li>
        <li class="contact__line">
          <svg class="contact__icon" viewBox="0 0 24 24"><path d="M7 2h10a2 2 0 0 1 2 2v16a2 2 0 0 1-2 2H7a2 2 0 0 1-2-2V4a2 2 0 0 1 2-2zm0 3v11h10V5zm5 13a1.2 1.2 0 1 0 0 2.4A1.2 1.2 0 0 0 12 18z"/></svg>
          555-019-4820
        </li>
        <li class="contact__line">
          <svg class="contact__icon" viewBox="0 0 24 24"><path d="M7 2h10v6H7zM4 9h16a2 2 0 0 1 2 2v7h-3v4H5v-4H2v-7a2 2 0 0 1 2-2zm3 7v4h10v-4z"/></svg>
          555-014-2790
        </li>
        <li class="contact__line">
          <svg class="contact__icon" viewBox="0 0 24 24"><path d="M2 5h20v14H2zm2 2v.5l8 5.5 8-5.5V7zm0 2.9V17h16V9.9l-8 5.5z"/></svg>
          lowell@stoneworkhaven.com
        </li>
      </ul>
    </div>
  </div>
</body>
</html>
```